Owner of Clinical Testing Lab/. Pixel Harbor Logo completed. Need Matching business Cards

Im the owner of and need cards for business. Colors fonts and logo already purchased through pixel harbor and have the source files. Like to keep same color format , Include logo one side. My Name Address of Lab. My cell number, Lab telephone number and website address. Want to keep simple.

Target Market(s)

Customers

Industry/Entity Type

HealthCare

Contact Information for Business Card

Dr. Corisande Threlkeld Ph.D. Address: QVT Foundry Campus 4417 Foundry Campus Loop Building 2600 Room 314. Baton Rouge LA 70931. Phone : 555.317.0942

Requirements
Must have
• Logo - Color same

```html
<!DOCTYPE html>
<html lang="en">
<head>
<meta charset="utf-8">
<title>Ligand Works – Business Card</title>
<link href="https://fonts.googleapis.com/css2?family=Montserrat:wght@400;500;700&display=swap" rel="stylesheet">
<style>
  :root {
    --navy: #0b4a82;
    --navy-deep: #0a4580;
    --teal: #5cc3a9;
    --teal-soft: #6fcdb3;
    --ink: #2c2c2c;
    --paper: #ffffff;
    --stage: #2a2a2a;
  }
  * { box-sizing: border-box; margin: 0; padding: 0; }
  html, body {
    width: 1200px; height: 780px; overflow: hidden;
    background: var(--stage);
    font-family: "Montserrat", sans-serif;
  }
  .stage {
    width: 1200px; height: 780px;
    display: flex; align-items: center; justify-content: center; gap: 40px;
  }
  .card {
    position: relative;
    width: 540px; height: 310px;
    border-radius: 26px;
    overflow: hidden;
    box-shadow: 0 14px 30px rgba(0,0,0,.45);
  }

  /* Front */
  .card--front {
    background: linear-gradient(200deg, var(--teal) 0%, #3f9aa0 40%, var(--navy-deep) 85%);
    display: flex; align-items: center; justify-content: center;
  }
  .brand {
    display: flex; align-items: center; gap: 12px;
    font-weight: 500; letter-spacing: .08em; text-transform: uppercase;
    white-space: nowrap;
  }
  .brand__dot { width: 14px; height: 14px; border-radius: 50%; flex: none; }
  .card--front .brand { color: var(--paper); font-size: 30px; }
  .card--front .brand__dot { background: var(--paper); }

  /* Back */
  .card--back { background: var(--paper); }
  .card--back .brand {
    position: absolute; top: 40px; right: 34px;
    color: var(--navy); font-size: 19px;
  }
  .card--back .brand__dot { background: var(--navy); width: 11px; height: 11px; }

  .helix-art {
    position: absolute; left: 310px; top: 86px;
    width: 230px; height: 112px;
    border-radius: 56px 0 0 56px;
    background: linear-gradient(90deg, var(--teal-soft) 0%, #3f8fa6 45%, var(--navy) 70%, var(--teal) 100%);
    opacity: .9;
  }

  .person {
    position: absolute; left: 32px; top: 150px;
    max-width: 265px;
  }
  .person__name {
    font-weight: 700; font-size: 16px; letter-spacing: .02em;
    color: var(--navy); text-transform: uppercase; white-space: nowrap;
  }
  .person__name .accent { color: var(--teal); }
  .person__title { font-size: 11px; color: var(--ink); margin-top: 2px; }

  .contacts {
    position: absolute; left: 56px; bottom: 26px;
    list-style: none; font-size: 10.5px; color: var(--ink); line-height: 1.35;
  }
  .contacts li { display: flex; align-items: flex-start; gap: 8px; margin-top: 6px; }
  .contacts .icon {
    flex: none; width: 16px; height: 16px; border-radius: 50%;
    display: flex; align-items: center; justify-content: center;
  }
  .icon--navy { background: var(--navy); }
  .icon--teal { background: var(--teal); }
  .icon svg { width: 9px; height: 9px; }
</style>
</head>
<body>
<main class="stage">

  <section class="card card--front">
    <div class="brand"><span class="brand__dot"></span>Ligand Works</div>
  </section>

  <section class="card card--back">
    <div class="helix-art" role="img" aria-label="Decorative DNA double helix illustration in navy and teal"></div>

    <div class="brand"><span class="brand__dot"></span>Ligand Works</div>

    <div class="person">
      <h1 class="person__name">Dr. Corisande <span class="accent">Threlkeld</span></h1>
      <p class="person__title">Ph.D.</p>
    </div>

    <ul class="contacts">
      <li>
        <span class="icon icon--navy">
          <svg viewBox="0 0 10 10"><path d="M2 1.2 L3.6 1 L4.3 3 L3.3 3.8 Q4.2 5.8 6.2 6.7 L7 5.7 L9 6.4 L8.8 8 Q5 8.4 1.6 4.6 Q1.2 2.8 2 1.2Z" fill="#fff"/></svg>
        </span>
        555.317.0942
      </li>
      <li>
        <span class="icon icon--teal">
          <svg viewBox="0 0 10 10"><rect x="1" y="2.2" width="8" height="5.6" rx=".6" fill="none" stroke="#fff" stroke-width="1"/><path d="M1.3 2.6 L5 5.4 L8.7 2.6" fill="none" stroke="#fff" stroke-width="1"/></svg>
        </span>
        youremailaddress@goes.here
      </li>
      <li>
        <span class="icon icon--navy">
          <svg viewBox="0 0 10 10"><path d="M5 9 Q1.6 5.4 1.6 3.7 A3.4 3.4 0 0 1 8.4 3.7 Q8.4 5.4 5 9Z" fill="#fff"/><circle cx="5" cy="3.7" r="1.2" fill="#0b4a82"/></svg>
        </span>
        <span>QVT Foundry Campus<br>4417 Foundry Campus Loop Building<br>2600 Room 314 . Baton Rouge LA 70931</span>
      </li>
    </ul>
  </section>

</main>
</body>
</html>
```